Vord Plix Business Cards
Vord Plix Stationary
Professional
Harold (Hal) Brennick
Director
Asia Pacific and Middle East
harold@vord-plix.com
www.vord-plix.com
I have thought about utilizing the four corners of the business card by putting name, phone, email address and url.
Possible full bleed.
would also like the back to say the following:
Oil&Gas Emergency Response Planning and Consulting.

```html
<!DOCTYPE html>
<html lang="en">
<head>
<meta charset="utf-8">
<title>Vord Plix Stationery</title>
<link rel="stylesheet" href="https://fonts.googleapis.com/css2?family=Exo+2:wght@700&family=Open+Sans:wght@400;600&display=swap">
<style>
  :root{
    --orange:#f05a1a;
    --black:#141414;
    --grey:#c9c9c9;
    --paper:#ffffff;
    --stage:#eef0f1;
    --ink:#555;
  }
  *{box-sizing:border-box;margin:0;padding:0}
  html,body{width:1200px;height:310px;overflow:hidden;background:var(--stage);font-family:"Open Sans",sans-serif;color:var(--ink)}
  .canvas{position:relative;width:1200px;height:310px}
  .item{position:absolute;background:var(--paper);box-shadow:0 1px 4px rgba(0,0,0,.25);overflow:hidden}
  .brand{font-family:"Exo 2",sans-serif;font-weight:700;color:var(--orange);letter-spacing:1px;white-space:nowrap;display:flex;align-items:center;gap:4px}
  .brand .dot{display:inline-block;border-radius:50%;background:var(--orange)}
  .swoosh{position:absolute;left:0;bottom:0;width:100%}
  .tiny{font-size:4px;line-height:1.4}

  /* master logo */
  .logo-block{position:absolute;left:12px;top:10px;width:180px;height:110px;display:flex;flex-direction:column;align-items:center;justify-content:center}
  .logo-block .brand{font-size:30px}
  .logo-block .brand .dot{width:22px;height:22px}
  .logo-block .tagline{font-size:9px;color:#777;margin-top:6px}

  /* business cards */
  .card-dark{background:var(--black);color:#ddd}
  .card-front{left:12px;top:137px;width:110px;height:72px}
  .card-front .brand{position:absolute;left:8px;top:10px;font-size:11px}
  .card-front .brand .dot{width:8px;height:8px}
  .card-front .name{position:absolute;left:8px;top:30px;font-size:5px;color:#fff;font-weight:600}
  .card-front .role{position:absolute;left:8px;top:37px;font-size:4px;color:#bbb}
  .card-back{left:12px;top:233px;width:112px;height:60px}
  .card-back .brand{position:absolute;left:8px;top:8px;font-size:10px}
  .card-back .brand .dot{width:7px;height:7px}
  .card-back .tiny{position:absolute;left:8px;bottom:8px;color:#ccc}
  .card-white{left:132px;top:233px;width:110px;height:60px}
  .card-white .corner{position:absolute;font-size:4px}
  .card-white .tl{left:6px;top:6px;font-weight:600;color:#222}
  .card-white .tr{right:6px;top:6px;text-align:right}
  .card-white .bl{left:6px;bottom:6px}
  .card-white .br{right:6px;bottom:6px;text-align:right}

  /* letterheads */
  .letterhead{top:19px;width:192px;height:274px}
  .letterhead .brand{position:absolute;left:14px;top:14px;font-size:9px}
  .letterhead .brand .dot{width:7px;height:7px}
  .letterhead .mark{position:absolute;left:56px;top:90px;width:80px;height:80px;border-radius:50%;background:var(--orange);opacity:.07}
  .letterhead .tiny{position:absolute;left:0;right:0;bottom:4px;text-align:center;color:#fff}
  .lh-1{left:264px}
  .lh-2{left:487px}

  /* compliment slips */
  .slip{left:701px;width:206px}
  .slip .brand{position:absolute;left:12px;top:10px;font-size:8px}
  .slip .brand .dot{width:6px;height:6px}
  .slip .tiny{position:absolute;left:0;right:0;bottom:3px;text-align:center;color:#fff}
  .slip-1{top:96px;height:108px}
  .slip-2{top:211px;height:82px}

  /* envelopes */
  .envelope{left:929px;width:259px}
  .env-dark{top:96px;height:50px;background:var(--black)}
  .env-dark .brand{position:absolute;left:50%;top:50%;transform:translate(-50%,-50%);font-size:10px}
  .env-dark .brand .dot{width:8px;height:8px}
  .env-flap{top:151px;height:66px}
  .env-flap .brand{position:absolute;left:50%;top:16px;transform:translateX(-50%);font-size:8px;color:#fff}
  .env-flap .brand .dot{width:6px;height:6px;background:#fff}
  .env-back{top:228px;height:65px}
  .env-back svg{position:absolute;inset:0;width:100%;height:100%}
</style>
</head>
<body>
<main class="canvas">

  <section class="logo-block">
    <div class="brand"><span class="dot"></span>VORD PLIX</div>
    <div class="tagline">Response Planning</div>
  </section>

  <article class="item card-dark card-front">
    <div class="brand"><span class="dot"></span>VORD PLIX</div>
    <div class="name">Harold (Hal) Brennick</div>
    <div class="role">Director · Asia Pacific and Middle East</div>
    <svg class="swoosh" viewBox="0 0 110 20" preserveAspectRatio="none" height="20"><path d="M0 20 L0 14 Q55 4 110 0 L110 20Z" fill="var(--orange)"/></svg>
  </article>

  <article class="item card-dark card-back">
    <div class="brand"><span class="dot"></span>VORD PLIX</div>
    <div class="tiny">Oil&amp;Gas Emergency Response Planning and Consulting.</div>
    <svg class="swoosh" viewBox="0 0 112 8" preserveAspectRatio="none" height="6"><rect width="112" height="8" fill="var(--orange)"/></svg>
  </article>

  <article class="item card-white">
    <div class="corner tl">Harold (Hal) Brennick<br><span style="font-weight:400;color:#777">Director</span></div>
    <div class="corner tr">+61 8 5550 0142</div>
    <div class="corner bl">harold@vord-plix.com</div>
    <div class="corner br">www.vord-plix.com</div>
    <svg class="swoosh" viewBox="0 0 110 10" preserveAspectRatio="none" height="4"><rect width="110" height="10" fill="var(--orange)"/></svg>
  </article>

  <article class="item letterhead lh-1">
    <div class="brand"><span class="dot"></span>VORD PLIX</div>
    <div class="mark" aria-hidden="true"></div>
    <svg class="swoosh" viewBox="0 0 192 40" preserveAspectRatio="none" height="40"><path d="M0 40 L0 18 Q100 30 192 2 L192 40Z" fill="var(--grey)"/><path d="M0 40 L0 26 Q100 34 192 10 L192 40Z" fill="var(--orange)"/></svg>
    <div class="tiny">Perth WA · www.vord-plix.com</div>
  </article>

  <article class="item letterhead lh-2">
    <div class="brand"><span class="dot"></span>VORD PLIX</div>
    <div class="mark" aria-hidden="true"></div>
    <svg class="swoosh" viewBox="0 0 192 40" preserveAspectRatio="none" height="40"><path d="M0 40 L0 18 Q100 30 192 2 L192 40Z" fill="var(--grey)"/><path d="M0 40 L0 26 Q100 34 192 10 L192 40Z" fill="var(--orange)"/></svg>
    <div class="tiny">Perth WA · www.vord-plix.com</div>
  </article>

  <article class="item slip slip-1">
    <div class="brand"><span class="dot"></span>VORD PLIX</div>
    <svg class="swoosh" viewBox="0 0 206 30" preserveAspectRatio="none" height="28"><path d="M0 30 L0 12 Q110 22 206 0 L206 30Z" fill="var(--grey)"/><path d="M0 30 L0 18 Q110 26 206 6 L206 30Z" fill="var(--orange)"/></svg>
    <div class="tiny">www.vord-plix.com</div>
  </article>

  <article class="item slip slip-2">
    <div class="brand"><span class="dot"></span>VORD PLIX</div>
    <svg class="swoosh" viewBox="0 0 206 30" preserveAspectRatio="none" height="26"><path d="M0 30 L0 12 Q110 22 206 0 L206 30Z" fill="var(--grey)"/><path d="M0 30 L0 18 Q110 26 206 6 L206 30Z" fill="var(--orange)"/></svg>
    <div class="tiny">www.vord-plix.com</div>
  </article>

  <article class="item envelope env-dark">
    <div class="brand"><span class="dot"></span>VORD PLIX</div>
  </article>

  <article class="item envelope env-flap">
    <svg style="position:absolute;inset:0;width:100%;height:100%" viewBox="0 0 259 66" preserveAspectRatio="none"><path d="M0 0 L259 0 L259 8 L129.5 40 L0 8Z" fill="var(--orange)"/></svg>
    <div class="brand"><span class="dot"></span>VORD PLIX</div>
  </article>

  <article class="item envelope env-back">
    <svg viewBox="0 0 259 65" preserveAspectRatio="none"><path d="M0 0 L129.5 34 L259 0" fill="none" stroke="#d5d5d5"/><path d="M0 65 L110 30 M259 65 L149 30" stroke="#e2e2e2" fill="none"/></svg>
  </article>

</main>
</body>
</html>
```